Redesign of Engineering firm website

I want a redesign of the torvelpower.com website with the below in mind:

1- the client has a 3 main sectors: Renewable Energy, Process Automation and General Engineering.
2- Home page should show the 3 sectors
3- the other standard pages should be home, About, Clients, Projects, Training, Career, and Contact
4- The theme should be wordpress.
5- Responsive layout that works with all devices
6- One page layout is preferable for the home page.
7- it should be original and is not copied from other templates.
Updates

Reason: As requested from so many designers... the deadline is extended. Thank you

Target Market(s)

Engineers and professional

Industry/Entity Type

Solar Energy

Font styles to use
Serif
Sans Serif

Colors
3277b5
0355a3
0493ce

Requirements
Must have
• pictures that represent the three sectors

```html
<!DOCTYPE html>
<html lang="en">
<head>
<meta charset="utf-8">
<title>Torvel Power</title>
<link rel="stylesheet" href="https://fonts.googleapis.com/css2?family=Oswald:wght@400;500;600&family=Open+Sans:wght@400;600;700&display=swap">
<style>
:root{
  --blue:#0355a3;
  --blue-mid:#3277b5;
  --blue-light:#0493ce;
  --blue-deep:#023f7d;
  --ink:#3a4250;
  --muted:#6b7584;
  --white:#ffffff;
  --line:#d7e3ef;
}
*{box-sizing:border-box;margin:0;padding:0}
html,body{width:1200px;height:2972px;overflow:hidden}
body{font-family:"Open Sans",Arial,sans-serif;color:var(--ink);background:var(--white);position:relative}
.heading{font-family:"Oswald","Arial Narrow",sans-serif;font-weight:500;letter-spacing:2px;text-transform:uppercase}

/* nav */
.nav{position:absolute;top:0;left:0;width:1200px;height:48px;background:var(--blue);display:flex;align-items:center;justify-content:space-between;padding:0 120px 0 240px;z-index:3}
.nav ul{display:flex;list-style:none;height:48px}
.nav li{font:600 11px "Open Sans",sans-serif;color:var(--white);letter-spacing:1px;padding:0 16px;display:flex;align-items:center}
.nav li.active{background:var(--blue-light)}
.nav .call{font:600 11px "Open Sans",sans-serif;color:var(--white);letter-spacing:1px}

/* hero */
.hero{position:absolute;top:48px;left:0;width:1200px;height:600px;background:linear-gradient(160deg,#5fa7dc 0%,#2f77b8 38%,#0b3f78 70%,#c79a2a 100%)}
.hero-text{position:absolute;top:176px;left:620px;width:440px;text-align:center;color:var(--white)}
.hero-text h1{font:600 62px "Oswald",sans-serif;letter-spacing:3px;line-height:1}
.hero-text p{font:600 18px "Open Sans",sans-serif;line-height:24px;margin-top:6px}
.brand-badge{position:absolute;top:610px;left:500px;width:200px;height:120px;background:var(--white);border-radius:6px;box-shadow:0 4px 12px rgba(0,0,0,.2);display:flex;align-items:center;justify-content:center;gap:10px;z-index:2}
.brand-badge .dot{width:18px;height:18px;border-radius:50%;background:var(--blue-light)}
.brand-badge span{font:600 24px "Oswald",sans-serif;color:var(--blue)}

/* about */
.about{position:absolute;top:760px;left:0;width:1200px;height:300px}
.about .photo{position:absolute;left:72px;top:60px;width:408px;height:170px;background:linear-gradient(135deg,#e8f4e4,#9fcf7c 55%,#5aa0d8)}
.about h2{position:absolute;left:560px;top:70px;width:560px;text-align:center;color:var(--blue);font-size:28px}
.about .copy{position:absolute;left:520px;top:118px;width:620px;font-size:10.5px;line-height:16px;color:var(--muted)}
.about .copy p+p{margin-top:8px}
.btn{display:inline-block;background:var(--blue-light);color:var(--white);font:600 10px "Open Sans",sans-serif;letter-spacing:1px;padding:7px 20px;text-transform:uppercase}
.about .btn{position:absolute;left:1020px;top:252px}

/* blue bands */
.band{position:absolute;left:0;width:1200px;background:linear-gradient(180deg,var(--blue-mid),var(--blue))}
.band h2{color:var(--white);text-align:center;font-size:30px;margin-top:34px}
.band .intro{width:720px;margin:12px auto 0;text-align:center;color:#dbe9f6;font-size:10.5px;line-height:16px}

.projects-band{top:1060px;height:330px}
.card-row{display:flex;gap:12px;width:720px;margin:18px auto 0}
.card{flex:1;background:var(--white)}
.card .pic{height:110px}
.card h3{font:700 9px "Open Sans",sans-serif;color:var(--blue);padding:8px 8px 2px;text-transform:uppercase}
.card p{font-size:7.5px;line-height:11px;color:var(--muted);padding:0 8px 8px}
.dots{display:flex;justify-content:center;gap:6px;margin-top:10px}
.dots i{width:6px;height:6px;border-radius:50%;background:rgba(255,255,255,.5)}
.dots i:first-child{background:var(--white)}

/* strategies */
.strategies{position:absolute;top:1390px;left:0;width:1200px;height:330px}
.strategies h2{position:absolute;left:240px;top:70px;color:var(--blue);font-size:28px}
.strategies .copy{position:absolute;left:240px;top:116px;width:440px;font-size:10.5px;line-height:16px;color:var(--muted)}
.strategies .copy p+p{margin-top:8px}
.strategies .btn{position:absolute;left:570px;top:262px}
.strategies .photo{position:absolute;left:720px;top:30px;width:240px;height:260px;background:linear-gradient(160deg,#d9eefc,#7fbf5a 60%,#3d8a3a)}

/* services */
.services-band{top:1720px;height:580px}
.service-row{display:flex;gap:18px;width:720px;margin:22px auto 0}
.service{flex:1;color:var(--white)}
.service .pic{height:180px}
.service h3{font:700 15px "Open Sans",sans-serif;margin-top:14px}
.service p{font-size:9px;line-height:14px;color:#dbe9f6;margin-top:6px}
.service .more{display:block;text-align:right;font-size:9px;font-weight:600;margin-top:8px}

/* clients */
.clients{position:absolute;top:2300px;left:0;width:1200px;height:240px;text-align:center}
.clients h2{color:var(--blue);font-size:28px;margin-top:30px}
.client-row{display:flex;justify-content:center;gap:40px;margin-top:30px}
.client{width:200px;height:100px;border:1px solid var(--line);display:flex;flex-direction:column;align-items:center;justify-content:center;gap:10px}
.client .mark{width:36px;height:36px;background:var(--blue-mid);border-radius:4px}
.client span{font-size:8px;font-weight:700;color:var(--ink);text-transform:uppercase}

/* contact */
.contact-band{top:2540px;height:400px}
.contact-band .sub{text-align:center;color:var(--white);font:600 13px "Open Sans",sans-serif;letter-spacing:2px;margin-top:6px;text-transform:uppercase}
.form{width:720px;margin:26px auto 0}
.fields{display:flex;gap:14px}
.field{flex:1;height:30px;background:var(--white);font-size:9px;color:var(--muted);padding:9px 10px}
.field.area{height:80px;margin-top:12px}
.form .send{display:block;width:90px;margin:12px auto 0;border:1px solid var(--white);color:var(--white);font-size:9px;text-align:center;padding:6px 0}
.address{text-align:center;color:var(--white);font-size:11px;line-height:18px;margin-top:16px}
.socials{display:flex;justify-content:center;gap:8px;margin-top:10px}
.socials i{width:20px;height:20px;border-radius:50%;background:var(--blue-light)}
.footer{position:absolute;top:2940px;left:0;width:1200px;height:32px;background:var(--blue-deep);color:#c9dbee;font-size:9px;display:flex;align-items:center;justify-content:space-between;padding:0 240px}
</style>
</head>
<body>

<header class="nav">
  <ul>
    <li class="active">HOME</li><li>ABOUT</li><li>CLIENTS</li><li>PROJECTS</li><li>TRAINING</li><li>CAREER</li><li>CONTACT</li>
  </ul>
  <div class="call">CALL US : +966 13 555 0142</div>
</header>

<section class="hero" role="img" aria-label="Photo of solar panels under a blue sky with sunflowers in the foreground">
  <div class="hero-text">
    <h1>TORVEL POWER</h1>
    <p>Harbor District, Eastern Province 31900<br>Kingdom of Saudi Arabia<br>Email : info@torvelpower.com<br>Phone : +966 13 555 0142</p>
  </div>
</section>
<div class="brand-badge"><i class="dot"></i><span>Torvel Power</span></div>

<section class="about">
  <div class="photo" role="img" aria-label="Light bulb with green leaves and a small solar panel"></div>
  <h2 class="heading">About Torvel Power</h2>
  <div class="copy">
    <p>We are the only engineering firm in the region that brings renewable energy, process automation and general engineering under one roof. Since our founding we have delivered projects for industry, education and housing across the Kingdom, with a team of certified engineers who design, build and maintain every system we supply.</p>
    <p>Our approach combines local knowledge with international standards, giving clients reliable plants, lower running costs and clear support from first study to final handover.</p>
  </div>
  <span class="btn">Read More</span>
</section>

<section class="band projects-band">
  <h2 class="heading">Services Client Projects</h2>
  <p class="intro">We provide design, supply, installation and maintenance for solar, automation and engineering projects, working closely with each client to meet budget, schedule and performance goals.</p>
  <div class="card-row">
    <div class="card"><div class="pic" role="img" aria-label="Solar panels in a field" style="background:linear-gradient(160deg,#8ec6ef,#2c6aa8)"></div><h3>Solar System Operations</h3><p>Daily monitoring and upkeep of working plants.</p></div>
    <div class="card"><div class="pic" role="img" aria-label="Solar array at sunset" style="background:linear-gradient(160deg,#f2c66a,#2a5f97)"></div><h3>Monitoring Maintenance</h3><p>Scheduled checks that keep output high.</p></div>
    <div class="card"><div class="pic" role="img" aria-label="Rows of solar panels" style="background:linear-gradient(160deg,#a9d6f4,#1b4f86)"></div><h3>Solar Design Engineering</h3><p>Layouts sized for site and load.</p></div>
    <div class="card"><div class="pic" role="img" aria-label="Solar farm development site" style="background:linear-gradient(160deg,#cfe6f7,#5a8fb8)"></div><h3>Solar Development</h3><p>Full delivery from permit to handover.</p></div>
  </div>
  <div class="dots"><i></i><i></i><i></i></div>
</section>

<section class="strategies">
  <h2 class="heading">Strategies Torvel Power</h2>
  <div class="copy">
    <p>Provide consistent service to meet and exceed client needs. Develop lasting partnerships through quality, safety and honest reporting on every project we take on.</p>
    <p>Grow our engineering skills through training so our people stay ahead of new tools, codes and clean energy methods used across the region.</p>
    <p>Support national goals for sustainable power by offering efficient, affordable systems to homes, schools and industry.</p>
  </div>
  <span class="btn">Read More</span>
  <div class="photo" role="img" aria-label="Hand holding a green globe with a small plant"></div>
</section>

<section class="band services-band">
  <h2 class="heading">Services</h2>
  <p class="intro">Torvel Power delivers three core sectors: renewable energy, process automation and general engineering, each backed by trained staff, proven partners and full after sales support for clients across the Kingdom.</p>
  <div class="service-row">
    <div class="service"><div class="pic" role="img" aria-label="Solar panels and wind turbines" style="background:linear-gradient(160deg,#9fd0f2,#2f73b0)"></div><h3>Renewable Energy</h3><p>Solar and hybrid systems for homes, farms and industry, designed for long life and steady output in local conditions.</p><span class="more">Read More</span></div>
    <div class="service"><div class="pic" role="img" aria-label="Industrial control panel and automated machinery" style="background:linear-gradient(160deg,#b6c7d8,#3b5a7c)"></div><h3>Process Automation</h3><p>Control systems, instruments and software that make plants safer, faster and easier to run every day.</p><span class="more">Read More</span></div>
    <div class="service"><div class="pic" role="img" aria-label="Engineer at a power tower site" style="background:linear-gradient(160deg,#f3d27a,#3e7fb8)"></div><h3>General Engineering</h3><p>Electrical and mechanical works, studies and site supervision for projects of every size and sector.</p><span class="more">Read More</span></div>
  </div>
  <div class="dots"><i></i><i></i><i></i></div>
</section>

<section class="clients">
  <h2 class="heading">Projects Torvel Power</h2>
  <div class="client-row">
    <div class="client"><i class="mark"></i><span>Northgate Institute of Science</span></div>
    <div class="client"><i class="mark"></i><span>Solara Housing Project</span></div>
    <div class="client"><i class="mark"></i><span>Eastline University Solar Plant</span></div>
  </div>
</section>

<section class="band contact-band">
  <h2 class="heading">Contact Us</h2>
  <p class="sub">Send an email. All fields with an * are required.</p>
  <div class="form">
    <div class="fields"><div class="field">Your Name *</div><div class="field">Your Email *</div><div class="field">Subject *</div></div>
    <div class="field area">Your Message Here *</div>
    <span class="send">Send Message</span>
  </div>
  <p class="address">Location : Harbor District, Eastern Province 31900 Kingdom of Saudi Arabia<br>Phone : +966 13 555 0142 &nbsp;-&nbsp; E-Mail : info@torvelpower.com</p>
  <div class="socials"><i></i><i></i><i></i><i></i></div>
</section>

<footer class="footer"><span>Copyright © Torvel Power. All Rights Reserved.</span><span>Privacy Policy | Terms of Use</span></footer>

</body>
</html>
```